Tech business card design

We need an amazing business card design for our new business 'Brakka' a marketing tech startup based in Sydney, Australia. We provide an online marketplace for businesses to search and buy advertising media, connect with service providers and learn more about marketing. We wish to communicate 'cool tech', reliability and professionalism and design based around our logo.

Target Market(s)

Business Owners

Contact Information for Business Card

Name
Position
Email Address
Website
Phone Number

Font styles to use
Other font styles liked:
• Avenir & Avenir Next

Colors

Designer to choose colors to be used in the design.

```html
<!DOCTYPE html>
<html lang="en">
<head>
<meta charset="utf-8">
<title>Brakka Business Card</title>
<link rel="stylesheet" href="https://fonts.googleapis.com/css2?family=Nunito+Sans:wght@400;600;800;900&display=swap">
<style>
  :root {
    --navy: #0f1c45;
    --paper: #ffffff;
    --backdrop: #e6e3df;
    --ink-soft: #4a5068;
    --rule: #1b2550;
  }
  * { margin: 0; padding: 0; box-sizing: border-box; }
  html, body {
    width: 1200px; height: 997px; overflow: hidden;
    background: var(--backdrop);
    font-family: "Nunito Sans", "Avenir Next", Avenir, sans-serif;
  }
  .sheet {
    position: relative; width: 1200px; height: 997px;
    display: flex; flex-direction: column; align-items: center; justify-content: center; gap: 80px;
  }
  .card {
    position: relative; width: 640px; height: 366px;
    box-shadow: 0 4px 14px rgba(0,0,0,0.12);
  }
  .card--front {
    background: var(--navy);
    display: flex; align-items: center; justify-content: center;
  }
  .wordmark {
    font-weight: 900; letter-spacing: -1px; line-height: 1;
  }
  .card--front .wordmark { color: var(--paper); font-size: 92px; }
  .card--back { background: var(--paper); color: var(--navy); }
  .card--back .wordmark {
    position: absolute; right: 64px; top: 38px;
    font-size: 68px; color: var(--navy);
  }
  .rule {
    position: absolute; height: 1.5px; background: var(--rule);
  }
  .rule--top { left: 200px; right: 44px; top: 124px; }
  .rule--bottom { left: 44px; width: 250px; top: 300px; }
  .contact {
    position: absolute; right: 44px; top: 142px;
    list-style: none; text-align: right;
    font-size: 14px; color: var(--ink-soft); line-height: 22px;
  }
  .contact li { display: flex; justify-content: flex-end; align-items: center; gap: 8px; }
  .contact svg { width: 13px; height: 13px; fill: var(--navy); }
  .person {
    position: absolute; left: 44px; top: 246px;
  }
  .person__name {
    font-size: 22px; font-weight: 800; letter-spacing: 0.5px; color: var(--navy); line-height: 1.1;
  }
  .person__role {
    font-size: 15px; color: var(--ink-soft); line-height: 1.3;
  }
</style>
</head>
<body>
<main class="sheet">
  <section class="card card--front">
    <span class="wordmark">brakka</span>
  </section>

  <section class="card card--back">
    <span class="wordmark">brakka</span>
    <div class="rule rule--top"></div>
    <ul class="contact">
      <li>000-555-0182
        <svg viewBox="0 0 16 16"><path d="M3 2h3l1.5 3.5-2 1.2a8 8 0 0 0 3.8 3.8l1.2-2L14 10v3a1 1 0 0 1-1 1A11 11 0 0 1 2 3a1 1 0 0 1 1-1z"/></svg>
      </li>
      <li>hello@brakka.co
        <svg viewBox="0 0 16 16"><path d="M1 3h14v10H1z M1.5 3.5 8 9l6.5-5.5" stroke="#fff" stroke-width="1.2"/></svg>
      </li>
      <li>www.brakka.co
        <svg viewBox="0 0 16 16"><circle cx="8" cy="8" r="7"/><path d="M1 8h14M8 1c-3 3.5-3 10.5 0 14M8 1c3 3.5 3 10.5 0 14" stroke="#fff" stroke-width="1" fill="none"/></svg>
      </li>
    </ul>
    <div class="person">
      <p class="person__name">MAREN ELLIS</p>
      <p class="person__role">Managing Director</p>
    </div>
    <div class="rule rule--bottom"></div>
  </section>
</main>
</body>
</html>
```